clean web design for a recruitment company

We need a web design for a company called 'TORAVI' recruitment. We are a new age recruitment companies that selects people by their true nature, values and what they can bring to the table as a tangible talent. We are all here possessing a certain talent, whatever that could be that the world needs. The final design should communicate professionalism and strongly embedded etiquette we believe in and a branding promise 'Seeing ones true nature'. Our companies values are integrity, giving away to the community, cherishing the sharing of our talent, time and helping one another.

Target Market(s)

Gulf Countries

Industry/Entity Type

It Company

Number of Pages Required

1 page

Font styles to use
Serif

Requirements
Must have
• Clear and readable font, user friendly structure and easy navigation menus.
Nice to have
• Extra sort of ideas on images we may use, tag lines etc. sample sites we love site:https://www.velmorandi.example/
• http://www.tessabrankow.example/
• http://www.pebbleloomcraft.example/idea-gallery/
Should not have
• all sort of colors, big combination of fonts, images with people in the office or people in suits likewise all the typical industry web sites

```html
<!DOCTYPE html>
<html lang="en">
<head>
<meta charset="utf-8">
<title>Toravi Recruitment</title>
<link href="https://fonts.googleapis.com/css2?family=Open+Sans:wght@400;600;700&family=Raleway:wght@300;400;600;700&display=swap" rel="stylesheet">
<style>
:root{
  --ink:#333333;
  --ink-soft:#666666;
  --muted:#8a8a8a;
  --rule:#d8d8d8;
  --nav-bg:#e4e4e4;
  --dark:#3b3b3b;
  --darker:#262626;
  --panel:rgba(40,40,40,.78);
  --link:#2a86d1;
  --paper:#ffffff;
  --gray-band:#e9e9e9;
}
*{box-sizing:border-box;margin:0;padding:0}
html,body{width:1200px;height:3945px;overflow:hidden}
body{position:relative;background:var(--paper);font-family:"Open Sans",Arial,sans-serif;color:var(--ink);font-size:13px;line-height:1.55}
.abs{position:absolute}
p{color:var(--ink-soft)}

/* header */
.site-header{left:0;top:0;width:1200px;height:108px}
.brand{left:165px;top:20px;display:flex;flex-direction:column;align-items:flex-start}
.brand-mark{width:34px;height:34px;background:var(--darker);margin-left:4px}
.brand-name{font-family:"Raleway",sans-serif;font-weight:700;font-size:22px;letter-spacing:2px;color:var(--darker);margin-top:4px}
.brand-sub{font-size:9px;letter-spacing:2px;color:var(--muted);text-transform:uppercase}
.account-links{right:150px;top:14px;display:flex;gap:16px;font-size:12px;color:var(--ink-soft);letter-spacing:1px;align-items:center}
.main-nav{left:0;top:108px;width:1200px;height:34px;background:var(--nav-bg);border-bottom:1px solid #cfcfcf}
.main-nav ul{list-style:none;display:flex;margin-left:165px;height:34px;align-items:center}
.main-nav li{font-size:12px;font-weight:600;letter-spacing:1px;color:var(--ink);padding:0 22px;border-right:1px solid #c9c9c9;line-height:14px}
.main-nav li:first-child{padding-left:0}
.main-nav li:last-child{border-right:0}

/* hero */
.hero{left:0;top:145px;width:1200px;height:463px;background:linear-gradient(180deg,#d9d9d9 0%,#a9a9a9 45%,#6e6e6e 100%)}
.hero-arrow{top:210px;width:30px;height:44px;background:rgba(0,0,0,.7);display:flex;align-items:center;justify-content:center}

/* welcome */
.section-title{font-family:"Raleway",sans-serif;font-weight:400;text-transform:uppercase;color:var(--ink);text-align:center;letter-spacing:2px}
.welcome-title{left:0;top:668px;width:1200px;font-size:38px;line-height:44px}
.welcome-col{top:775px;width:410px;font-size:13px;line-height:22px}

/* search */
.search-title{left:0;top:1062px;width:1200px;font-size:32px}
.search-title strong{font-weight:700}
.search-field{top:1130px;width:270px;height:34px;border:1px solid var(--rule);background:#f3f3f3;font-size:12px;color:var(--muted);display:flex;align-items:center;gap:8px;padding-left:10px}
.btn-find{left:532px;top:1190px;width:136px;height:44px;border:2px solid var(--darker);display:flex;align-items:center;justify-content:center;font-size:12px;font-weight:700;letter-spacing:1px;color:var(--darker)}
.advanced{left:0;top:1242px;width:1200px;text-align:center;font-size:11px;color:var(--muted)}

/* stats */
.stats{left:0;top:1306px;width:1200px;height:152px;background:linear-gradient(90deg,#3d3d3d,#262626 50%,#3d3d3d)}
.stat{top:1332px;width:260px;text-align:center;color:#fff}
.stat-num{font-family:"Open Sans",sans-serif;font-weight:700;font-size:40px;line-height:46px}
.stat-label{font-size:18px;font-weight:400;margin-top:4px}

/* video & blog */
.block-head{top:1505px;height:40px;display:flex;align-items:center;justify-content:space-between;width:430px}
.block-head h2{font-family:"Raleway",sans-serif;font-weight:400;font-size:26px;letter-spacing:1px;text-transform:uppercase}
.btn-more{display:flex;align-items:center;gap:6px;background:var(--dark);color:#fff;font-size:11px;font-weight:700;letter-spacing:1px;padding:5px 8px 5px 12px}
.video-frame{left:155px;top:1578px;width:430px;height:264px;background:linear-gradient(160deg,#e8eef3,#cfdde8 55%,#b9cad8)}
.play{left:325px;top:1680px;width:90px;height:60px;background:rgba(0,0,0,.55);display:flex;align-items:center;justify-content:center}
.video-caption{left:155px;top:1872px;font-family:"Open Sans",sans-serif;font-weight:700;font-size:14px;text-transform:uppercase}
.video-text{left:155px;top:1906px;width:430px;font-size:12px;line-height:20px}
.post-thumb{left:615px;width:150px;height:100px;background:linear-gradient(135deg,#dfe4ea,#aeb8c4)}
.post{left:782px;width:270px}
.post-date{font-size:11px;color:var(--muted)}
.post h3{font-size:14px;font-weight:700;line-height:18px;margin:4px 0 6px}
.post p{font-size:12px;line-height:18px}
.post a{color:var(--link);text-decoration:none}

/* categories */
.cat-title{left:0;top:2128px;width:1200px;font-size:32px}
.cat-list{top:2208px;list-style:none;font-size:12px;line-height:25px;color:var(--ink-soft)}
.cat-list li::before{content:"›";margin-right:6px}

/* why */
.why{left:0;top:2402px;width:1200px;height:608px;background:linear-gradient(100deg,#5a5a5a 0%,#8e8e8e 40%,#c9c9c9 62%,#7c7c7c 100%)}
.why-panel{left:158px;top:2444px;width:484px;height:527px;background:var(--panel);padding:26px 36px;color:#fff}
.why-panel h2{font-family:"Raleway",sans-serif;font-weight:400;font-size:34px;letter-spacing:2px;text-align:center;margin-bottom:18px}
.why-item{margin-bottom:30px}
.why-item h3{display:flex;align-items:center;gap:10px;font-size:17px;font-weight:700;margin-bottom:6px}
.why-item p{color:#e6e6e6;font-size:12px;line-height:18px;padding-left:2px}
.tick{width:22px;height:22px;background:#fff;display:flex;align-items:center;justify-content:center}

/* clients */
.clients{left:0;top:3010px;width:1200px;height:650px;background:var(--gray-band)}
.clients-title{left:0;top:3082px;width:1200px;font-size:30px}
.quote{background:#fff;box-shadow:0 1px 3px rgba(0,0,0,.15)}
.quote-head{height:38px;background:var(--dark);color:#fff;display:flex;align-items:center;justify-content:flex-end;padding-right:18px;font-weight:700;font-size:17px;position:relative}
.quote-mark{position:absolute;top:-6px;left:14px;font-family:Georgia,serif;font-size:64px;line-height:64px;color:#fff}
.quote-body{padding:18px 28px 20px 28px;font-size:13px;line-height:20px;color:var(--ink-soft);font-style:italic;position:relative}
.quote-end{position:absolute;right:16px;bottom:-8px;font-family:Georgia,serif;font-size:64px;line-height:64px;color:#d6d6d6}
.clients-more{left:562px;top:3614px}

/* footer */
.footer-col{top:3682px;font-size:12px;line-height:20px;color:var(--ink-soft)}
.footer-col h4{font-size:12px;font-weight:700;letter-spacing:1px;color:var(--ink);text-transform:uppercase;margin-bottom:6px}
.footer-col .date{font-size:10px;color:var(--muted)}
.social{display:flex;gap:6px}
.social span{width:22px;height:22px;border-radius:50%;background:#9a9a9a;display:block}
.copyright{left:0;top:3905px;width:1200px;text-align:center;font-size:11px;color:var(--ink-soft)}
.footer-rule{left:165px;top:3890px;width:870px;height:1px;background:var(--rule)}
</style>
</head>
<body>

<header class="site-header abs">
  <div class="brand abs">
    <span class="brand-mark"></span>
    <span class="brand-name">TORAVI</span>
    <span class="brand-sub">recruitment</span>
  </div>
  <div class="account-links abs">
    <span>LOGIN</span><span>REGISTER</span>
    <svg width="12" height="12" viewBox="0 0 12 12"><circle cx="5" cy="5" r="3.6" fill="none" stroke="#666" stroke-width="1.5"/><line x1="7.6" y1="7.6" x2="11" y2="11" stroke="#666" stroke-width="1.5"/></svg>
  </div>
</header>

<nav class="main-nav abs">
  <ul>
    <li>HOME</li><li>TEAM</li><li>METHODOLOGY</li><li>SPECIALIST AREAS</li><li>CLIENTS</li><li>CANDIDATES</li><li>TORAVI GROUP</li>
  </ul>
</nav>

<div class="hero abs" role="img" aria-label="Gallery wall of framed black and white portrait photographs"></div>
<div class="hero-arrow abs" style="left:0;top:355px"><svg width="12" height="18" viewBox="0 0 12 18"><polyline points="10,2 3,9 10,16" fill="none" stroke="#fff" stroke-width="3"/></svg></div>
<div class="hero-arrow abs" style="left:1170px;top:355px"><svg width="12" height="18" viewBox="0 0 12 18"><polyline points="2,2 9,9 2,16" fill="none" stroke="#fff" stroke-width="3"/></svg></div>

<h1 class="section-title welcome-title abs">Welcome to<br>Toravi Recruitment</h1>
<p class="welcome-col abs" style="left:165px">Lorem ipsum dolor sit amet, consectetur adipisicing elit, sed do eiusmod tempor incididunt ut labore et dolore magna aliqua. Ut enim ad minim veniam, quis nostrud exercitation ullamco laboris nisi ut aliquip ex ea commodo consequat. Duis aute irure dolor in reprehenderit in voluptate velit esse cillum dolore eu fugiat nulla pariatur. Excepteur sint occaecat cupidatat non proident, sunt in culpa qui officia deserunt mollit anim id est laborum.</p>
<p class="welcome-col abs" style="left:625px">Lorem ipsum dolor sit amet, consectetur adipisicing elit, sed do eiusmod tempor incididunt ut labore et dolore magna aliqua. Ut enim ad minim veniam, quis nostrud exercitation ullamco laboris nisi ut aliquip ex ea commodo consequat. Duis aute irure dolor in reprehenderit in voluptate velit esse cillum dolore eu fugiat nulla pariatur. Excepteur sint occaecat cupidatat non proident, sunt in culpa qui officia deserunt mollit anim id est laborum.</p>

<h2 class="section-title search-title abs">Search through <strong>855,172</strong> jobs</h2>
<div class="search-field abs" style="left:330px">
  <svg width="11" height="11" viewBox="0 0 12 12"><circle cx="5" cy="5" r="3.6" fill="none" stroke="#999" stroke-width="1.5"/><line x1="7.6" y1="7.6" x2="11" y2="11" stroke="#999" stroke-width="1.5"/></svg>Keywords, title or company</div>
<div class="search-field abs" style="left:606px">
  <svg width="10" height="13" viewBox="0 0 10 13"><path d="M5 12 C2 8 1 6 1 4.5 A4 4 0 0 1 9 4.5 C9 6 8 8 5 12Z" fill="#999"/><circle cx="5" cy="4.5" r="1.4" fill="#f3f3f3"/></svg>City, state or postal code</div>
<div class="btn-find abs">FIND JOBS</div>
<div class="advanced abs">Advanced Search ›</div>

<div class="stats abs" role="img" aria-label="Dark mosaic of candidate portrait photographs"></div>
<div class="stat abs" style="left:160px"><div class="stat-num">1,000,000</div><div class="stat-label">Candidates</div></div>
<div class="stat abs" style="left:470px"><div class="stat-num">60,000</div><div class="stat-label">Roles Recruited</div></div>
<div class="stat abs" style="left:780px"><div class="stat-num">5,000</div><div class="stat-label">Satisfied Clients</div></div>

<div class="block-head abs" style="left:155px"><h2>Our Video</h2><span class="btn-more">MORE <svg width="8" height="10" viewBox="0 0 8 10"><polygon points="0,0 8,5 0,10" fill="#fff"/></svg></span></div>
<div class="block-head abs" style="left:615px"><h2>From the Blog</h2><span class="btn-more">MORE <svg width="8" height="10" viewBox="0 0 8 10"><polygon points="0,0 8,5 0,10" fill="#fff"/></svg></span></div>

<div class="video-frame abs" role="img" aria-label="Video still: illustration of business people running towards a goal"></div>
<div class="play abs"><svg width="20" height="24" viewBox="0 0 20 24"><polygon points="0,0 20,12 0,24" fill="#fff"/></svg></div>
<h3 class="video-caption abs">What goes wrong on a hard drive?</h3>
<p class="video-text abs">Sed ut perspiciatis unde omnis iste natus error sit voluptatem accusantium doloremque laudantium, totam rem aperiam, eaque ipsa quae ab illo inventore veritatis et quasi architecto beatae vitae dicta sunt explicabo. Sed ut perspiciatis unde omnis iste natus error sit voluptatem accusantium doloremque laudantium, totam rem aperiam.</p>

<div class="post-thumb abs" style="top:1578px" role="img" aria-label="Blog thumbnail: people at a meeting"></div>
<article class="post abs" style="top:1574px"><div class="post-date">1/9/2015</div><h3>Lorem ipsum dolor sit amet, consectetur adipiscing elit</h3><p>Sed ut perspiciatis unde omnis iste natus error sit voluptatem accusantium doloremque laudantium. <a>Read more</a></p></article>
<div class="post-thumb abs" style="top:1735px" role="img" aria-label="Blog thumbnail: team working at desks"></div>
<article class="post abs" style="top:1731px"><div class="post-date">1/9/2015</div><h3>Lorem ipsum dolor sit amet, consectetur adipiscing elit</h3><p>Sed ut perspiciatis unde omnis iste natus error sit voluptatem accusantium doloremque laudantium. <a>Read more</a></p></article>
<div class="post-thumb abs" style="top:1895px" role="img" aria-label="Blog thumbnail: people in conversation"></div>
<article class="post abs" style="top:1891px"><div class="post-date">1/9/2015</div><h3>Lorem ipsum dolor sit amet, consectetur adipiscing elit</h3><p>Sed ut perspiciatis unde omnis iste natus error sit voluptatem accusantium doloremque laudantium. <a>Read more</a></p></article>

<h2 class="section-title cat-title abs">Job Searching Categories</h2>
<ul class="cat-list abs" style="left:280px"><li>Job Search Basics</li><li>Kickstart Your Job Search</li><li>Job Listings</li><li>Best Jobs</li><li>Cover Letters</li><li>Resumes</li></ul>
<ul class="cat-list abs" style="left:592px"><li>Job Applications</li><li>Job Interviews</li><li>Career Advice</li><li>Letter and Email Examples</li><li>Employment References</li><li>Curriculum Vitae</li></ul>
<ul class="cat-list abs" style="left:872px"><li>Leaving Your Job</li><li>Salary &amp; Benefits</li><li>Skills, Abilities &amp; Keywords</li><li>Find a Job</li><li>How to Apply for a Job</li><li>Resumes and Cover Letters</li></ul>

<div class="why abs" role="img" aria-label="Photograph of a smiling young professional seated with a tablet"></div>
<section class="why-panel abs">
  <h2>WHY CHOOSE US?</h2>
  <div class="why-item"><h3><span class="tick"><svg width="14" height="12" viewBox="0 0 14 12"><polyline points="1,6 5,10 13,1" fill="none" stroke="#333" stroke-width="2.5"/></svg></span>Over 50 years of experience</h3><p>Lorem ipsum dolor sit amet, consectetur adipiscing elit, sed do eiusmod tempor incididunt ut labore et dolore magna aliqua.</p></div>
  <div class="why-item"><h3><span class="tick"><svg width="14" height="12" viewBox="0 0 14 12"><polyline points="1,6 5,10 13,1" fill="none" stroke="#333" stroke-width="2.5"/></svg></span>We are passionate</h3><p>Lorem ipsum dolor sit amet, consectetur adipiscing elit, sed do eiusmod tempor incididunt ut labore et dolore magna aliqua.</p></div>
  <div class="why-item"><h3><span class="tick"><svg width="14" height="12" viewBox="0 0 14 12"><polyline points="1,6 5,10 13,1" fill="none" stroke="#333" stroke-width="2.5"/></svg></span>We are fast, accurate &amp; reliable</h3><p>Lorem ipsum dolor sit amet, consectetur adipiscing elit, sed do eiusmod tempor incididunt ut labore et dolore magna aliqua.</p></div>
  <div class="why-item"><h3><span class="tick"><svg width="14" height="12" viewBox="0 0 14 12"><polyline points="1,6 5,10 13,1" fill="none" stroke="#333" stroke-width="2.5"/></svg></span>We are improving everyday</h3><p>Lorem ipsum dolor sit amet, consectetur adipiscing elit, sed do eiusmod tempor incididunt ut labore et dolore magna aliqua.</p></div>
</section>

<div class="clients abs"></div>
<h2 class="section-title clients-title abs">What our clients are saying</h2>
<div class="quote abs" style="left:72px;top:3165px;width:560px"><div class="quote-head"><span class="quote-mark">“</span>Jeremy, NJ</div><div class="quote-body">Lorem ipsum dolor sit amet, consectetur adipiscing elit, sed do eiusmod tempor incididunt ut labore et dolore magna aliqua. Ut enim ad minim veniam, quis nostrud exercitation ullamco laboris nisi ut aliquip ex ea commodo consequat. Duis aute irure dolor in reprehenderit velit esse.<span class="quote-end">”</span></div></div>
<div class="quote abs" style="left:642px;top:3191px;width:493px"><div class="quote-head"><span class="quote-mark">“</span>Jim, DE</div><div class="quote-body">Lorem ipsum dolor sit amet, consectetur adipiscing elit, sed do eiusmod tempor incididunt ut labore et dolore magna aliqua.<span class="quote-end">”</span></div></div>
<div class="quote abs" style="left:158px;top:3410px;width:457px"><div class="quote-head"><span class="quote-mark">“</span>Andy, NJ</div><div class="quote-body">Lorem ipsum dolor sit amet, consectetur adipiscing elit, sed do eiusmod tempor incididunt ut labore et dolore magna aliqua.<span class="quote-end">”</span></div></div>
<div class="quote abs" style="left:642px;top:3395px;width:493px"><div class="quote-head"><span class="quote-mark">“</span>Tom &amp; Lisa, NYC</div><div class="quote-body">Lorem ipsum dolor sit amet, consectetur adipiscing elit, sed do eiusmod tempor incididunt ut labore et dolore magna aliqua.<span class="quote-end">”</span></div></div>
<span class="btn-more clients-more abs">MORE <svg width="8" height="10" viewBox="0 0 8 10"><polygon points="0,0 8,5 0,10" fill="#fff"/></svg></span>

<footer>
  <div class="footer-col abs" style="left:165px"><h4>Company</h4>Our Story<br>Login<br>Sitemap<br>Privacy</div>
  <div class="footer-col abs" style="left:276px"><h4>Job Seekers</h4>Our Services<br>Job Search<br>Upload Your Resume<br>FAQs</div>
  <div class="footer-col abs" style="left:444px;width:200px"><h4>Latest News</h4>Lorem ipsum dolor sit amet, consectetur adipiscing elit.<br><span class="date">Apr 15, 2015</span><br>Lorem ipsum dolor sit amet, consectetur adipiscing elit.<br><span class="date">Apr 15, 2015</span></div>
  <div class="footer-col abs" style="left:665px;width:200px"><h4>Contact Us</h4>Questions? 888 888 8888<br>Careers: careers@toravi.example<br><br>1000 Lorem Ipsum,<br>Nulla aliquet 22222 USA</div>
  <div class="footer-col abs" style="left:888px"><h4>Follow Us</h4><div class="social"><span></span><span></span><span></span><span></span></div></div>
  <div class="footer-rule abs"></div>
  <div class="copyright abs">Copyright © 2015 toravi recruitment. All Rights Reserved.</div>
</footer>

</body>
</html>
```